Financial Advisor Resource Firm needs business card design

Need business card design for company in Omaha NE called Tallowbrook Partners. We provide resources to financial advisors....workshop programs, retirement analysis, and insurance planning. I would like to see designs that use grays, greens, black, and white colors. The final design should communicate 'collaboration' and be simple yet attractive to financial planning clients. I will attached our logo and another picture of a puzzle piece coming together. I would like the incorporate the puzzle picture somehow, maybe on the back somehow, with color or just the gray scale....OR, the picture be the front of the card with 'Tallowbrook' definition on it (see upload) and then company logo, employee name, title, address on the back (see ppt uploaded). The following disclosure needs to be included somewhere- Advisory services offered through Marlowe Ridge Advisors, LLC.
Updates

I uploaded a svg and ai file of the logo

Target Market(s)

Financial planning clients and financial advisors....so pretty diverse age range of about 40-70.

Industry/Entity Type

Financial Planning

Contact Information for Business Card

Dennis K. Holloway, MBA
Founder/President
5727 E. Larkspur Avenue
Suite 418
Omaha, NE 68297
Phone- (402) 555-0147
Cell- (402) 555-0183
Fax- (402) 555-0129
email- dennis@tallowbrookgroup.example
web address- www.tallowbrookgroup.example

Colors
1b1b1b
474747
d3d3d3
ffffff
9bcb3c
abd036

Requirements
Must have
• Must include logo provided, must be 2 sided, and must have disclosure...all of these items listed in project description

```html
<!DOCTYPE html>
<html lang="en">
<head>
<meta charset="utf-8">
<title>Tallowbrook Partners – Business Card</title>
<link rel="stylesheet" href="https://fonts.googleapis.com/css2?family=Cinzel:wght@600;700&family=Arimo:wght@400;700&display=swap">
<style>
  :root {
    --ink: #1b1b1b;
    --graphite: #474747;
    --mist: #d3d3d3;
    --paper: #ffffff;
    --leaf: #9bcb3c;
    --lime: #abd036;
    --stage: #ecece8;
  }
  * { box-sizing: border-box; margin: 0; padding: 0; }
  html, body { width: 1200px; height: 880px; overflow: hidden; }
  body {
    position: relative;
    background: var(--stage);
    font-family: "Arimo", Arial, sans-serif;
    color: var(--ink);
  }
  .card {
    position: absolute;
    width: 640px;
    height: 366px;
    border-radius: 22px;
    overflow: hidden;
    box-shadow: 0 14px 30px rgba(0,0,0,.18);
  }

  /* Front */
  .card-front { left: 60px; top: 50px; background: var(--leaf); }
  .front-photo {
    position: absolute; inset: 0;
    background: linear-gradient(120deg, #a6d265 0%, #8fc04f 45%, #6f9e3c 100%);
  }
  .front-brand {
    position: absolute; left: 0; right: 0; top: 160px;
    display: flex; align-items: center; justify-content: center; gap: 14px;
  }
  .brand-dot {
    width: 22px; height: 22px; border-radius: 50%;
    background: var(--paper);
  }
  .brand-name {
    font-family: "Cinzel", Georgia, serif;
    font-weight: 700;
    letter-spacing: 1px;
    text-transform: uppercase;
  }
  .front-brand .brand-name { font-size: 30px; color: var(--ink); }

  /* Back */
  .card-back { left: 500px; top: 464px; background: var(--paper); }
  .back-brand {
    position: absolute; left: 60px; top: 62px;
    display: flex; align-items: center; gap: 10px;
  }
  .back-brand .brand-dot { width: 18px; height: 18px; background: var(--leaf); }
  .back-brand .brand-name { font-size: 26px; color: var(--ink); }
  .rule {
    position: absolute; left: 150px; right: 40px; top: 160px;
    height: 2px; background: var(--leaf);
  }
  .edge-tab {
    position: absolute; left: -24px; top: 178px;
    width: 48px; height: 48px; border-radius: 50%;
    background: var(--leaf);
  }
  .person { position: absolute; left: 60px; top: 176px; }
  .person-name {
    font-family: "Cinzel", Georgia, serif; font-weight: 600;
    font-size: 19px; color: var(--ink); letter-spacing: .5px;
  }
  .person-title { font-size: 15px; color: var(--leaf); margin-top: 3px; }

  .details {
    position: absolute; left: 60px; right: 30px; top: 248px;
    display: flex; font-size: 13px; line-height: 21px; color: var(--ink);
  }
  .details-col { padding: 0 16px; border-left: 1px solid var(--mist); }
  .details-col:first-child { padding-left: 0; border-left: none; }
  .phones li { list-style: none; display: flex; align-items: center; gap: 8px; }
  .icon {
    width: 17px; height: 17px; border-radius: 50%;
    background: var(--leaf); display: inline-flex; align-items: center; justify-content: center;
  }
  .icon svg { width: 10px; height: 10px; fill: var(--paper); }
  .address { font-style: normal; }
  .web .accent { color: var(--leaf); }
  .online { font-size: 12.5px; }

  .disclosure {
    position: absolute; left: 60px; right: 30px; top: 330px;
    font-size: 10.5px; line-height: 14px; color: var(--graphite);
  }
</style>
</head>
<body>

<section class="card card-front" aria-label="Card front">
  <div class="front-photo" role="img" aria-label="Green-toned photograph of two hands joining puzzle pieces"></div>
  <div class="front-brand">
    <span class="brand-dot"></span>
    <span class="brand-name">Tallowbrook Partners</span>
  </div>
</section>

<section class="card card-back" aria-label="Card back">
  <div class="back-brand">
    <span class="brand-dot"></span>
    <span class="brand-name">Tallowbrook Partners</span>
  </div>
  <div class="rule"></div>
  <div class="edge-tab"></div>

  <div class="person">
    <p class="person-name">DENNIS K. HOLLOWAY, MBA</p>
    <p class="person-title">Founder/President</p>
  </div>

  <div class="details">
    <ul class="details-col phones">
      <li><span class="icon"><svg viewBox="0 0 10 10"><path d="M2 0.5 L3.6 2.6 L2.8 3.6 Q4 6 6.4 7.2 L7.4 6.4 L9.5 8 L8.4 9.5 Q3 8.6 0.5 1.6 Z"/></svg></span>(402) 555-0147</li>
      <li><span class="icon"><svg viewBox="0 0 10 10"><rect x="2.5" y="0.5" width="5" height="9" rx="1"/></svg></span>(402) 555-0183</li>
      <li><span class="icon"><svg viewBox="0 0 10 10"><rect x="2.5" y="0.5" width="5" height="3"/><rect x="0.5" y="4" width="9" height="4" rx="1"/><rect x="2.5" y="7" width="5" height="2.5"/></svg></span>(402) 555-0129</li>
    </ul>
    <address class="details-col address">
      5727 E. Larkspur Avenue<br>Suite 418<br>Omaha, NE 68297
    </address>
    <div class="details-col online">
      <p>dennis@tallowbrookgroup.example</p>
      <p class="web">www.<span class="accent">tallowbrookgroup</span>.example</p>
    </div>
  </div>

  <p class="disclosure">Advisory services offered through Marlowe Ridge Advisors, LLC.</p>
</section>

</body>
</html>
```